Need Business Cards for my Business

email address: rkpmarlowhollowworks@vendrimail.com
web address: rkpmarlowhollowworks.net
Slogan: We offer various QVN licenses
Rowland K. Pemberly
Please stick with colors of Company Logo
would like the card to be more of the color example of the logo.
If you need PDF copy of logo email me at the above account.
Creative control rests with you.

Industry/Entity Type

Business

Contact Information for Business Card

I am a minimalist, but would like something to pop and stand out amongst other cards, make it memorable.

Font styles to use
Serif
Decorative
Script

```html
<!DOCTYPE html>
<html lang="en">
<head>
<meta charset="utf-8">
<title>Rowland K. Pemberly — Business Cards</title>
<link rel="stylesheet" href="https://fonts.googleapis.com/css2?family=Arimo:wght@400;700&family=Poiret+One&display=swap">
<style>
  :root {
    --page-bg: #ffffff;
    --card-bg: #ffffff;
    --card-edge: #e4e4e4;
    --card-shadow: rgba(0, 0, 0, 0.45);
    --ink: #111111;
    --name-grey: #6a6a6a;
    --accent-cyan: #3ec6df;
  }
  * { margin: 0; padding: 0; box-sizing: border-box; }
  html, body {
    width: 1200px;
    height: 1066px;
    overflow: hidden;
    background: var(--page-bg);
  }
  .canvas {
    position: relative;
    width: 1200px;
    height: 1066px;
  }
  .card {
    position: absolute;
    top: 75px;
    width: 525px;
    height: 853px;
    background: var(--card-bg);
    border: 1px solid var(--card-edge);
    box-shadow: 5px 6px 7px var(--card-shadow);
  }
  .card--front { left: 56px; }
  .card--back { left: 620px; }

  .front-mark {
    position: absolute;
    top: 125px;
    left: 50%;
    transform: translateX(-50%);
    width: 46px;
    height: 46px;
  }
  .holder-name {
    position: absolute;
    top: 468px;
    width: 100%;
    text-align: center;
    font-family: "Poiret One", sans-serif;
    font-size: 40px;
    letter-spacing: 0.5px;
    color: var(--name-grey);
  }
  .contact {
    position: absolute;
    top: 690px;
    width: 100%;
    text-align: center;
    font-family: "Arimo", sans-serif;
    font-size: 18px;
    line-height: 24px;
    color: var(--accent-cyan);
  }

  .company-name {
    position: absolute;
    top: 400px;
    width: 100%;
    text-align: center;
    font-family: "Arimo", sans-serif;
    font-weight: 700;
    font-size: 38px;
    letter-spacing: 1px;
    color: var(--ink);
  }
  .slogan {
    position: absolute;
    top: 752px;
    width: 100%;
    text-align: center;
    font-family: "Arimo", sans-serif;
    font-size: 20px;
    color: var(--ink);
  }
</style>
</head>
<body>
  <main class="canvas">
    <section class="card card--front" aria-label="Card front">
      <svg class="front-mark" viewBox="0 0 46 46" aria-hidden="true">
        <circle cx="23" cy="23" r="22" fill="var(--ink)"/>
      </svg>
      <p class="holder-name">Rowland K. Pemberly</p>
      <div class="contact">
        <p class="contact__web">rkpmarlowhollowworks.net</p>
        <p class="contact__email">rkpmarlowhollowworks@vendrimail.com</p>
      </div>
    </section>

    <section class="card card--back" aria-label="Card back">
      <p class="company-name">MARLOW HOLLOW WORKS</p>
      <p class="slogan">We Offer Various QVN Licenses</p>
    </section>
  </main>
</body>
</html>
```